First North America Product Category Rule

8 x 10 foot booth design for a stretch fabric wrap-around. The booth will be used in a very small exhibit area for 150 attendees. It is for the packaging industry focused on the environment. This booth graphic is NOT about our company, but to promote participation in a project we are sponsoring. The project is to develop the first North American Packaging Category Rule, so the booth is to invite conference attendees to join our effort. Production specifications are attached.

Target Market(s)

Meridian 300, Sustainability Directors, Packaging Engineers

Industry/Entity Type

Packaging; Environment

Font styles to use
Sans Serif

Requirements
Must have
• An Eye-Catching or Intriguing Image/Graphics/Letter Treatment
Should not have
• Nothing too bright or garish. All text should be above waist height (No text below the 36-40" mark)

```html
<!DOCTYPE html>
<html lang="en">
<head>
<meta charset="utf-8">
<title>First North American PCR – Booth Graphic</title>
<link rel="stylesheet" href="https://fonts.googleapis.com/css2?family=Barlow:ital,wght@0,300;0,600;0,700;1,700&family=Barlow+Condensed:wght@700&family=Noto+Sans:wght@700&family=Oswald:wght@600;700&family=Poppins:wght@500&display=swap">
<style>
  :root {
    --page: #eeeeee;
    --ink: #111111;
    --panel: #e6e6e6;
    --panel-shade: #cfcfcf;
    --mustard: #c4a702;
    --navy: #34548a;
    --navy-deep: #2a4a7a;
    --ribbon: #367100;
    --ribbon-edge: #5aa000;
    --olive: #556e18;
    --olive-deep: #475d12;
    --tagline: #3f5a0a;
    --lobe-pcr: #909b12;
    --lobe-lca: #ae840c;
    --lobe-edp: #5a2a1c;
    --lobe-verify: #5585a2;
    --quote-box: rgba(62, 46, 0, 0.82);
    --white: #ffffff;
  }
  html, body { margin: 0; padding: 0; width: 1200px; height: 800px; overflow: hidden; background: var(--page); }
  .booth-sheet { display: block; width: 1200px; height: 800px; }
  .label { font-family: "Noto Sans", sans-serif; font-weight: 700; font-size: 56px; fill: var(--ink); letter-spacing: 2px; }
  .headline { font-family: "Oswald", sans-serif; font-weight: 600; fill: var(--white); }
  .kicker { font-family: "Oswald", sans-serif; font-weight: 700; fill: var(--white); }
  .cta { font-family: "Barlow Condensed", sans-serif; font-weight: 700; fill: var(--white); }
  .tagline { font-family: "Barlow", sans-serif; font-weight: 700; font-style: italic; fill: var(--tagline); }
  .step-label { font-family: "Barlow", sans-serif; font-weight: 700; font-size: 23px; fill: var(--white); text-anchor: middle; }
  .step-num { font-family: "Poppins", sans-serif; font-weight: 500; font-size: 36px; fill: #333; text-anchor: middle; }
  .quote-text { font-family: "Barlow", sans-serif; font-weight: 600; font-size: 23px; fill: var(--white); }
  .quote-mark { font-family: "Barlow Condensed", sans-serif; font-weight: 700; font-size: 110px; fill: var(--white); }
  .credit-role { font-family: "Barlow", sans-serif; font-weight: 300; font-size: 34px; fill: var(--white); text-anchor: middle; }
  .credit-name { font-family: "Barlow", sans-serif; font-weight: 700; font-size: 34px; fill: var(--white); text-anchor: middle; }
</style>
</head>
<body>
<svg class="booth-sheet" viewBox="0 0 2352 1568" xmlns="http://www.w3.org/2000/svg">
  <defs>
    <filter id="booth-shadow" x="-5%" y="-5%" width="110%" height="110%">
      <feDropShadow dx="-10" dy="8" stdDeviation="6" flood-color="#000" flood-opacity="0.45"/>
    </filter>
    <linearGradient id="warehouse-tones" x1="0" y1="0" x2="1" y2="1">
      <stop offset="0" stop-color="#a78560"/>
      <stop offset="0.45" stop-color="#8c6c50"/>
      <stop offset="0.75" stop-color="#9c8a46"/>
      <stop offset="1" stop-color="#b08d66"/>
    </linearGradient>
  </defs>

  <text class="label" x="1172" y="170" text-anchor="middle">front viewable area</text>
  <rect x="536" y="206" width="1292" height="8" fill="var(--ink)"/>

  <g class="booth" filter="url(#booth-shadow)">
    <rect x="222" y="245" width="1908" height="1077" fill="var(--panel)"/>
  </g>

  <g class="booth-art">
    <polygon class="return-shade" points="222,245 288,245 535,1122 222,1122" fill="var(--panel-shade)"/>

    <polygon class="mustard-field" points="728,245 1790,245 2128,1322 1868,1322 1690,625 830,625" fill="var(--mustard)"/>

    <polygon class="photo-area" role="img" aria-label="Photo: warehouse worker in hard hat and safety vest scanning shrink-wrapped pallets"
             points="583,625 1682,625 1868,1322 535,1322 535,700" fill="url(#warehouse-tones)"/>

    <polygon class="title-band" points="955,245 2130,245 2130,428 848,428 830,372" fill="var(--navy)"/>
    <rect x="1818" y="245" width="312" height="183" fill="var(--navy-deep)" opacity="0.5"/>

    <text class="headline" x="895" y="380" font-size="74" textLength="925" lengthAdjust="spacingAndGlyphs">Enlisting Stakeholder Participation</text>
    <text class="kicker" x="918" y="512" font-size="88" textLength="758" lengthAdjust="spacingAndGlyphs">FIRST NORTH AMERICAN</text>

    <polygon class="tagline-strip" points="773,528 1803,528 1822,593 792,593" fill="var(--white)"/>
    <text class="tagline" x="845" y="575" font-size="40" textLength="905" lengthAdjust="spacingAndGlyphs">Product Category Rule (PCR) For Protective Packaging</text>

    <g class="signup-ribbon">
      <polygon points="450,590 795,245 955,245 450,750" fill="var(--ribbon)"/>
      <polygon points="450,740 945,245 955,245 450,750" fill="var(--ribbon-edge)"/>
      <text class="cta" x="0" y="0" font-size="92" text-anchor="middle" transform="translate(690,450) rotate(-45)">SIGN UP NOW</text>
    </g>

    <g class="quote-card">
      <polygon points="1480,712 1815,712 1910,1055 1495,1055" fill="var(--quote-box)"/>
      <text class="quote-mark" x="1532" y="822">“</text>
      <text class="quote-text" x="1535" y="805">
        <tspan x="1535" dy="0">How EPD Can Move the</tspan>
        <tspan x="1535" dy="32">Dialogue Beyond</tspan>
        <tspan x="1535" dy="32">End-of-Life Disposal to</tspan>
        <tspan x="1535" dy="32">Include Environmental</tspan>
        <tspan x="1535" dy="32">Benchmarks for</tspan>
        <tspan x="1535" dy="32">Product Production &amp;</tspan>
        <tspan x="1535" dy="32">Distribution</tspan>
      </text>
      <text class="quote-mark" x="1728" y="1080">”</text>
    </g>

    <g class="process-steps">
      <circle cx="675" cy="755" r="117" fill="var(--lobe-pcr)"/>
      <rect x="675" y="755" width="117" height="117" fill="var(--lobe-pcr)"/>
      <circle cx="922" cy="755" r="117" fill="var(--lobe-lca)"/>
      <rect x="805" y="755" width="117" height="117" fill="var(--lobe-lca)"/>
      <circle cx="675" cy="1002" r="117" fill="var(--lobe-edp)"/>
      <rect x="675" y="885" width="117" height="117" fill="var(--lobe-edp)"/>
      <circle cx="922" cy="1002" r="117" fill="var(--lobe-verify)"/>
      <rect x="805" y="885" width="117" height="117" fill="var(--lobe-verify)"/>

      <circle cx="758" cy="839" r="34" fill="var(--white)"/>
      <circle cx="840" cy="839" r="34" fill="var(--white)"/>
      <circle cx="758" cy="918" r="34" fill="var(--white)"/>
      <circle cx="840" cy="918" r="34" fill="var(--white)"/>
      <text class="step-num" x="758" y="852">01</text>
      <text class="step-num" x="840" y="852">02</text>
      <text class="step-num" x="758" y="931">04</text>
      <text class="step-num" x="840" y="931">03</text>

      <text class="step-label" x="675" y="737"><tspan x="675">PCR</tspan><tspan x="675" dy="26">Product Category</tspan><tspan x="675" dy="28">Rules</tspan></text>
      <text class="step-label" x="922" y="737"><tspan x="922">LCA</tspan><tspan x="922" dy="26">Life Cycle</tspan><tspan x="922" dy="28">Assessment</tspan></text>
      <text class="step-label" x="675" y="984"><tspan x="675">EDP</tspan><tspan x="675" dy="26">Registration and</tspan><tspan x="675" dy="28">Publication</tspan></text>
      <text class="step-label" x="922" y="996"><tspan x="922">Third Party</tspan><tspan x="922" dy="30">Verification</tspan></text>
    </g>

    <g class="credits-band">
      <polygon points="222,1122 1722,1122 1778,1322 222,1322" fill="var(--olive)"/>
      <polygon points="535,1122 1222,1122 1276,1322 592,1322" fill="var(--olive-deep)"/>
      <text class="credit-role" x="977" y="1170">Sponsored by</text>
      <text class="credit-name" x="977" y="1213">Foam Packaging Council</text>
      <text class="credit-role" x="1477" y="1170">Managed by</text>
      <text class="credit-name" x="1477" y="1213">Clearpath Ledger</text>
    </g>

    <line class="panel-fold" x1="535" y1="245" x2="535" y2="1322" stroke="#c8c8c8" stroke-width="2"/>
    <line class="panel-fold" x1="1818" y1="245" x2="1818" y2="1322" stroke="#c8c8c8" stroke-width="2" opacity="0.6"/>
  </g>

  <text class="label" x="893" y="1445">8 x 10 foot booth</text>
</svg>
</body>
</html>
```